Vemra. Packaging for mood-boosting energy drink mix. Upbeat and uplifting.

I need a mockup of a pouch package + a stick. I included an image of a Aqua Tarn pouch + stick for reference. I do not have a die line for the pouch, so feel free to just use the same relative dimensions for the pouch and create a rendering. Here are the specifications for the packaging that I need:
1. The logo is included in the uploaded files. Please use the one that says "bright day spark" beneath "vemra." The logo should take up about the top 1/3 to 1/2 of the pouch.
2. The pouch should be mostly white, especially behind the logo, but feel free to explore yellow or orange for the bottom 1/2 to 2/3 of the packaging.
3. In the center of the packaging, below the logo, please have the product name appear, "mood-boosting energy drink mix" similar to where "Fluid Amplifier" is placed.
4. Below that, create an image of a glass with a stick pouring into it like in the Aqua Tarn pouch.
5. Below the glass, in the bottom center of the package, include "16 sticks. Net Wt. 4 oz. (114 g)
6. On the left side, please include callouts, from top to bottom, "energy blend (80mg caffeine, taurine) + happy blend (saffron, st. john's wort, rhodiola).
7. On the right side, please include callouts, from top to bottom, "electrolytes + vitamins + 0g sugar"
8. Somewhere else on the front of the packaging, please include the flavor name "golden berry," perhaps where they do on the aqua tarn pouch.
9. For the stick, use your creativity.
10. There is no back of packaging to design for this project.

Target Market(s)

My target consumer leads a very active lifestyle and cares deeply about health & wellness.

Colors
0094D4
00A9DD
6FCCEA
C7EBF8
E9F6FB
FFC000
F8CF3A
FAE287
FDF2CF
FEFAEE
F0912C
F2A743
F7CA91
FBE8D2
FDF5EE
EE7325
F08F49
F5BC92
FAE3D3
FDF4ED

Requirements
Must have
• My packaging must make people feel good and maybe even smile when they see it. A brand that does this well is Penn. (www.pennvita-example.com)
Nice to have
• I like 60's Mod Design if you need some inspiration. The packaging should also convey a sense of levity. Like you'll float or dance through life after drinking this.

```html
<!DOCTYPE html>
<html lang="en">
<head>
<meta charset="utf-8">
<title>Vemra – Golden Berry Pouch and Stick</title>
<link rel="stylesheet" href="https://fonts.googleapis.com/css2?family=Nunito:wght@700;800;900&family=Arimo:wght@400;700&display=swap">
<style>
  :root {
    --orange-deep: #EE7325;
    --orange: #F0912C;
    --orange-soft: #F2A743;
    --gold: #FFC000;
    --gold-warm: #F8CF3A;
    --gold-pale: #FAE287;
    --cream: #FDF2CF;
    --cream-light: #FEFAEE;
    --flavor: #E3A21A;
    --ink: #111111;
    --film: #F4F4F4;
    --film-edge: #E2E2E2;
    --page: #FFFFFF;
  }
  html, body {
    margin: 0;
    padding: 0;
    width: 1200px;
    height: 1010px;
    overflow: hidden;
    background: var(--page);
  }
  .canvas { display: block; width: 1200px; height: 1010px; }
  .brand-name { font-family: "Nunito", sans-serif; font-weight: 900; fill: var(--orange-deep); }
  .tagline { font-family: "Nunito", sans-serif; font-weight: 700; fill: var(--orange); }
  .product-name { font-family: "Nunito", sans-serif; font-weight: 900; fill: var(--orange-deep); letter-spacing: 0.5px; }
  .callout { font-family: "Arimo", sans-serif; font-size: 20px; fill: var(--ink); }
  .callout-head { font-weight: 700; }
  .count-big { font-family: "Arimo", sans-serif; font-weight: 700; font-size: 27px; fill: var(--ink); }
  .count-small { font-family: "Arimo", sans-serif; font-size: 19px; fill: var(--ink); }
  .benefits { font-family: "Arimo", sans-serif; font-weight: 700; font-size: 20px; fill: var(--ink); }
  .flavor-name { font-family: "Nunito", sans-serif; font-weight: 900; font-size: 46px; fill: var(--flavor); letter-spacing: 1px; }
  .stick-flavor { font-family: "Nunito", sans-serif; font-weight: 800; font-size: 15px; fill: var(--orange-deep); letter-spacing: 0.5px; }
</style>
</head>
<body>
<svg class="canvas" viewBox="0 0 1200 1010" xmlns="http://www.w3.org/2000/svg">
  <defs>
    <linearGradient id="pouch-fill" x1="0" y1="0" x2="0" y2="1">
      <stop offset="0" stop-color="#FFFFFF"/>
      <stop offset="0.5" stop-color="#FFFFFF"/>
      <stop offset="0.62" stop-color="#FEF4D2"/>
      <stop offset="0.78" stop-color="#F9D860"/>
      <stop offset="1" stop-color="#F5BE2A"/>
    </linearGradient>
    <radialGradient id="glow-left" cx="0.5" cy="0.5" r="0.5">
      <stop offset="0" stop-color="#FFF3B0"/>
      <stop offset="1" stop-color="#FFFFFF" stop-opacity="0"/>
    </radialGradient>
    <linearGradient id="glass-fill" x1="0" y1="0" x2="0" y2="1">
      <stop offset="0" stop-color="#FBF7EC"/>
      <stop offset="1" stop-color="#F6C65A"/>
    </linearGradient>
  </defs>

  <g class="pouch">
    <path d="M160 80 Q160 68 175 68 L855 68 Q868 68 868 80 L866 960 Q866 985 845 985 L175 985 Q154 985 154 960 Z" fill="url(#pouch-fill)" stroke="var(--film-edge)" stroke-width="2"/>
    <rect x="160" y="70" width="706" height="128" fill="var(--film)"/>
    <line x1="160" y1="198" x2="866" y2="198" stroke="var(--film-edge)" stroke-width="2"/>

    <ellipse cx="290" cy="470" rx="210" ry="150" fill="url(#glow-left)"/>

    <text class="brand-name" x="300" y="345" font-size="170">vemra</text>
    <text class="tagline" x="517" y="382" font-size="27">bright day spark</text>

    <text class="product-name" x="470" y="446" font-size="30">MOOD-BOOSTING</text>
    <text class="product-name" x="470" y="480" font-size="30">ENERGY DRINK MIX</text>

    <rect role="img" aria-label="Glass of golden drink with orange splashes" x="432" y="500" width="225" height="215" rx="10" fill="url(#glass-fill)"/>

    <circle cx="300" cy="600" r="148" fill="var(--gold-warm)"/>
    <circle cx="300" cy="600" r="132" fill="var(--cream-light)"/>

    <rect role="img" aria-label="Single drink stick tilted over the glass" x="230" y="380" width="185" height="46" rx="4" fill="#FFFFFF" stroke="var(--film-edge)" transform="rotate(28 322 403)"/>

    <text class="callout">
      <tspan class="callout-head" x="200" y="519">Energy blend</tspan>
      <tspan x="200" y="544">(80mg caffeine,</tspan>
      <tspan x="200" y="569">taurine)</tspan>
      <tspan class="callout-head" x="200" y="595">Happy blend</tspan>
      <tspan x="200" y="619">(saffron,</tspan>
      <tspan x="200" y="644">st. John's wort,</tspan>
      <tspan x="200" y="669">rhodiola)</tspan>
    </text>

    <circle cx="768" cy="592" r="98" fill="var(--orange-soft)"/>
    <circle cx="768" cy="592" r="84" fill="var(--cream)"/>
    <text class="count-big" text-anchor="middle"><tspan x="768" y="556">16</tspan><tspan x="768" y="586">sticks</tspan></text>
    <text class="count-small" text-anchor="middle"><tspan x="768" y="618">Net Wt. 4 oz.</tspan><tspan x="768" y="645">(114 g)</tspan></text>

    <text class="benefits" text-anchor="end">
      <tspan x="806" y="728">Electrolytes</tspan>
      <tspan x="806" y="753">Vitamins</tspan>
      <tspan x="812" y="779">0g sugar</tspan>
    </text>

    <circle cx="525" cy="815" r="172" fill="var(--gold-warm)"/>
    <circle cx="525" cy="815" r="152" fill="var(--cream-light)"/>
    <text class="flavor-name" text-anchor="middle"><tspan x="512" y="826">GOLDEN</tspan><tspan x="512" y="874">BERRY</tspan></text>
  </g>

  <g class="stick">
    <path d="M932 238 L1112 238 L1114 884 L928 884 Z" fill="var(--film)" stroke="var(--film-edge)" stroke-width="2"/>
    <rect x="935" y="262" width="175" height="598" fill="#FFFFFF"/>
    <text class="stick-flavor" x="1019" y="357" text-anchor="middle">GOLDEN BERRY</text>
    <text class="brand-name" font-size="80" transform="translate(1050 630) rotate(-90)">vemra</text>
    <text class="tagline" font-size="17" transform="translate(1074 512) rotate(-90)">bright day spark</text>
    <text class="product-name" font-size="16" transform="translate(1018 822) rotate(-90)">MOOD-BOOSTING</text>
    <text class="product-name" font-size="16" transform="translate(1040 822) rotate(-90)">ENERGY DRINK MIX</text>
  </g>
</svg>
</body>
</html>
```